We’re a real estate firm that has landed a big builder in a neighboring state. Our branding needs...

We are a real estate firm who represents various builders along with doing resale here in Oregon. Our firm is growing to represent a big builder in Washington State and we’ll have another 40 brokers on our team. We need rebranding. As in, a new logo ( the house logo we have now looks cartoonish, hate it). We need new cards, something to really stand out. I’ve been thinking of using those NFC cards from ZIB or the ones with the seam color. I likely want two or three designs, a darker (as in a background color of black or grey) , a light one ( again I mean background color) and a credit card style (either plastic w an embossed name/number on front, or metal ). I’m thinking dark background for cc, or silver if it’s metal. That’s my thoughts, but you are the artists, so maybe you have an idea I haven’t considered. Our colors were black and red, but we don’t have to stick to that. Just nothing too busy. Oh, and we are typically representing the local, higher quality builders in our area (just below custom), but not national. Subdivisions are near the Kel Varsby, Tobrin, and Ashfield Coastal sites. We are super excited, but without a lot of time to change the “look” of our brokerage. So I’ll be deciding and moving forward within 24 hours tops. Our name is Real Estate Summitline Partners ( we cant change the name because of timeline and business license) Thank you!

Industry/Entity Type

Real Estate

Contact Information for Business Card

The usual. Name of firm. Name of cardholder. Contact info.

Font styles to use
Serif
Sans Serif

Colors

Designer to choose colors to be used in the design.

Requirements
Must have
• A sleek or simple look. I included photos of cards with stylistic attributes we like. Thank you
Nice to have
• We really like the black backgrounds. With foil or embossed detail. We also like the black on black. Matte black card with raised shiny black detail. But still eye catching.
Should not have
• No ornate or busy looking style. We don’t want anything cluttered.

```html
<!DOCTYPE html>
<html lang="en">
<head>
<meta charset="utf-8">
<title>Real Estate Summitline Partners — Business Cards</title>
<link href="https://fonts.googleapis.com/css2?family=Montserrat:wght@400;500;700&display=swap" rel="stylesheet">
<style>
  :root {
    --stage: #1b1b1d;
    --card: #262628;
    --card-edge: #303033;
    --white: #f4f4f4;
    --red: #e0262b;
    --grey: #9a9a9c;
    --gold: #cfa52e;
  }
  * { margin: 0; padding: 0; box-sizing: border-box; }
  html, body {
    width: 1200px; height: 865px; overflow: hidden;
    background: var(--stage);
    font-family: "Montserrat", Arial, sans-serif;
  }
  .stage { position: relative; width: 1200px; height: 865px; }

  .card {
    position: absolute;
    width: 560px; height: 320px;
    background: var(--card);
    border: 1px solid var(--card-edge);
    box-shadow: 0 18px 40px rgba(0,0,0,.55);
  }
  .card--front { left: 110px; top: 90px; }
  .card--back  { left: 530px; top: 470px; }

  /* Front */
  .holder { position: absolute; right: 34px; top: 34px; text-align: right; }
  .holder__name { font-weight: 700; font-size: 24px; letter-spacing: 1px; color: var(--white); }
  .holder__name .surname { color: var(--red); }
  .holder__title { font-size: 11px; letter-spacing: 2px; color: var(--grey); margin-top: 2px; }

  .address { position: absolute; left: 34px; top: 100px; display: flex; gap: 8px;
    font-size: 12px; line-height: 1.35; color: var(--white); }
  .address svg { flex: none; margin-top: 2px; }

  .firm-mark { position: absolute; right: 34px; top: 150px; width: 250px;
    font-weight: 500; font-size: 22px; line-height: 1.15; color: var(--white);
    text-transform: uppercase; letter-spacing: 1px; text-align: right; }

  .contacts { position: absolute; left: 34px; bottom: 30px; list-style: none;
    font-size: 12px; line-height: 1.55; color: var(--white); }
  .contacts li { display: flex; align-items: center; gap: 9px; }
  .contacts svg { flex: none; }

  /* Back */
  .firm-mark--gold { position: absolute; left: 70px; top: 80px;
    font-weight: 500; font-size: 34px; line-height: 1.15; letter-spacing: 2px;
    color: var(--gold); text-transform: uppercase; }
  .web { position: absolute; left: 70px; bottom: 36px;
    font-size: 14px; letter-spacing: 2px; color: var(--gold); }
</style>
</head>
<body>
<main class="stage">

  <section class="card card--front" aria-label="Business card front">
    <div class="holder">
      <div class="holder__name">JORDAN <span class="surname">VALE</span></div>
      <div class="holder__title">REAL ESTATE BROKER</div>
    </div>

    <div class="address">
      <svg width="10" height="13" viewBox="0 0 10 13" aria-hidden="true">
        <path d="M5 0a5 5 0 0 0-5 5c0 3.6 5 8 5 8s5-4.4 5-8a5 5 0 0 0-5-5z" fill="var(--red)"/>
        <circle cx="5" cy="5" r="1.8" fill="var(--card)"/>
      </svg>
      <p>1840 Harlow Avenue<br>Suite 305, Salem<br>OR 97301</p>
    </div>

    <div class="firm-mark">Real Estate Summitline Partners</div>

    <ul class="contacts">
      <li>
        <svg width="12" height="12" viewBox="0 0 12 12" aria-hidden="true"><path d="M2.5 0.5l2 2.5-1.2 1.5a7 7 0 0 0 4.2 4.2L9 7.5l2.5 2-1 2C5 11.5.5 7 .5 1.5z" fill="var(--red)"/></svg>
        555-381-0627
      </li>
      <li>
        <svg width="12" height="12" viewBox="0 0 12 12" aria-hidden="true"><rect x="3" y="0.5" width="6" height="3" fill="var(--red)"/><rect x="0.5" y="4" width="11" height="5" rx="1" fill="var(--red)"/><rect x="3" y="8" width="6" height="3.5" fill="var(--red)"/></svg>
        555-712-5394
      </li>
      <li>
        <svg width="12" height="10" viewBox="0 0 12 10" aria-hidden="true"><rect x="0.5" y="0.5" width="11" height="9" fill="var(--red)"/><path d="M0.5 0.5L6 5.5 11.5 0.5" fill="none" stroke="var(--card)" stroke-width="1.2"/></svg>
        info@summitlinepartners.com
      </li>
      <li>
        <svg width="12" height="12" viewBox="0 0 12 12" aria-hidden="true"><circle cx="6" cy="6" r="5.3" fill="none" stroke="var(--red)" stroke-width="1.3"/><ellipse cx="6" cy="6" rx="2.3" ry="5.3" fill="none" stroke="var(--red)" stroke-width="1"/><line x1="0.7" y1="6" x2="11.3" y2="6" stroke="var(--red)" stroke-width="1"/></svg>
        www.SummitlinePartners.com
      </li>
    </ul>
  </section>

  <section class="card card--back" aria-label="Business card back">
    <div class="firm-mark--gold">Real Estate<br>Summitline<br>Partners</div>
    <div class="web">WWW.SUMMITLINEPARTNERS.COM</div>
  </section>

</main>
</body>
</html>
```